Business Card Design Project

Hi Designers, this project is currently on hold until the Logo is completed:
Please submit to the Logo project here:
http://jobs.pixelmarket.example/job.aspx?id=371905

Once logo is completed, it will be attached to this project for you to create business cards with show logo, company name and address

Maren T K Ashdown

Corwin's Meadow Pine Flock Co.
Hazelmere
Upper Brackwell
North Devon EX21 4TN

Tel: 01809 351846
Mobile: 07912 463078
email: maren@meadow-pine-flock.example
Updates

Project Deadline Extended
Reason: Sorry everyone, we have had a sick ewe and I am now behind with this one and need to extend the deadline. Best wishes Maren

The designer who wins the logo brief will be asked to design the business card. Many thanks Maren

Project Deadline Extended
Reason: Sorry everyone, just a chaotic time of year with animals. Need to extend the deadline again..... as I just haven't had enough time to take a good look.... Thank you for your understanding. Maren

Project Deadline Extended
Reason: Sorry everyone It is our busiest time of year with animals and just no time to spend going through such great designs. I will have to extend the deadline again and hopefully have some news very soon. Wishing you all a very happy Christmas and a happy and healthy new year. Maren & Corwin

Target Market(s)

High end market
Boutique restaurants for meat (it's not commercial lamb it's a slow matured quality meat more like venison/beef) expensive - specialized market

High End shoot clothing / wool / sheepskin rugs
Quality products

Industry/Entity Type

Business

Requirements
Must have
• based on the logo - (which Pixel Market has just been asked to do)
possibly based on a simplified picture of a Hebridean Ram (shows it's a Hebridean by it's horns as opposed to other black sheep!!)

```html
<!DOCTYPE html>
<html lang="en">
<head>
<meta charset="utf-8">
<title>Corwin's Meadow Pine Flock Co. — Business Cards</title>
<link href="https://fonts.googleapis.com/css2?family=Lato:wght@300;400;700&display=swap" rel="stylesheet">
<style>
  :root {
    --backdrop: #e9e6e1;
    --card-white: #ffffff;
    --card-white-shade: #eeeeee;
    --card-black: #0c0c0c;
    --card-black-sheen: #2a2a2a;
    --ink: #2b2b2b;
    --ink-soft: #6b6b6b;
    --mark-faint: #e4e4e4;
    --mark-white: #f4f4f4;
  }
  * { box-sizing: border-box; margin: 0; padding: 0; }
  html, body {
    width: 1200px; height: 1023px; overflow: hidden;
    background: var(--backdrop);
    font-family: 'Lato', sans-serif;
    color: var(--ink);
  }
  .canvas { position: relative; width: 1200px; height: 1023px; }
  .card {
    position: absolute;
    width: 560px; height: 350px;
    border-radius: 22px;
    overflow: hidden;
    box-shadow: 0 10px 28px rgba(0,0,0,0.18);
  }
  .card--front {
    left: 80px; top: 150px;
    background: linear-gradient(160deg, var(--card-white) 40%, var(--card-white-shade));
  }
  .card--back {
    left: 560px; top: 520px;
    background: linear-gradient(160deg, var(--card-black-sheen) 0%, var(--card-black) 45%);
  }
  .faint-circle {
    position: absolute; right: 36px; top: 34px;
    width: 190px; height: 190px;
  }
  .brand {
    position: absolute; display: flex; align-items: center; gap: 12px;
  }
  .card--front .brand { left: 30px; top: 30px; }
  .brand-name {
    font-weight: 300; text-transform: uppercase; letter-spacing: 0.06em;
    line-height: 1.05;
  }
  .card--front .brand-name { font-size: 22px; color: var(--ink-soft); }
  .brand-name small { display: block; font-size: 0.5em; letter-spacing: 0.18em; }
  .holder { position: absolute; left: 30px; top: 118px; }
  .holder-name { font-weight: 700; font-size: 19px; }
  .holder-role { font-size: 14px; color: var(--ink-soft); margin-top: 2px; }
  .contacts {
    position: absolute; left: 30px; top: 182px;
    list-style: none; font-size: 14px; line-height: 22px;
  }
  .contacts li { display: flex; align-items: center; gap: 8px; }
  .contacts svg { width: 13px; height: 13px; flex: none; }
  .address {
    position: absolute; left: 30px; top: 282px;
    font-size: 14px; line-height: 19px; font-style: normal;
  }
  .card--back .brand {
    left: 50%; top: 50%; transform: translate(-50%, -50%);
    flex-direction: row-reverse; gap: 22px;
  }
  .card--back .brand-name { font-size: 30px; color: #d9d9d9; text-align: right; }
</style>
</head>
<body>
<main class="canvas">
  <section class="card card--front" aria-label="Business card front">
    <svg class="faint-circle" viewBox="0 0 100 100" aria-hidden="true">
      <circle cx="50" cy="50" r="46" fill="none" stroke="var(--mark-faint)" stroke-width="5"/>
    </svg>
    <div class="brand">
      <svg width="58" height="58" viewBox="0 0 100 100" aria-hidden="true">
        <circle cx="50" cy="50" r="44" fill="none" stroke="#9a9a9a" stroke-width="6"/>
      </svg>
      <div class="brand-name">Corwin's<small>Meadow Pine Flock Co.</small></div>
    </div>
    <div class="holder">
      <div class="holder-name">Maren T K Ashdown</div>
      <div class="holder-role">Director</div>
    </div>
    <ul class="contacts">
      <li><svg viewBox="0 0 16 16"><path d="M3 1h3l1 4-2 1a9 9 0 0 0 5 5l1-2 4 1v3a2 2 0 0 1-2 2A13 13 0 0 1 1 3a2 2 0 0 1 2-2z" fill="#333"/></svg>01809 351846</li>
      <li><svg viewBox="0 0 16 16"><rect x="4" y="1" width="8" height="14" rx="1.5" fill="none" stroke="#333" stroke-width="1.5"/></svg>07912 463078</li>
      <li><svg viewBox="0 0 16 16"><rect x="1" y="3" width="14" height="10" fill="none" stroke="#333" stroke-width="1.5"/><path d="M1 3l7 6 7-6" fill="none" stroke="#333" stroke-width="1.5"/></svg>maren@meadow-pine-flock.example</li>
      <li><svg viewBox="0 0 16 16"><rect x="1.5" y="1.5" width="13" height="13" fill="none" stroke="#333" stroke-width="1.5"/></svg>www.meadow-pine-flock.example</li>
    </ul>
    <address class="address">
      Corwin's Meadow Pine Flock Co.<br>
      Hazelmere, Upper Brackwell<br>
      North Devon EX21 4TN
    </address>
  </section>

  <section class="card card--back" aria-label="Business card back">
    <div class="brand">
      <svg width="150" height="150" viewBox="0 0 100 100" aria-hidden="true">
        <circle cx="50" cy="50" r="44" fill="none" stroke="var(--mark-white)" stroke-width="6"/>
      </svg>
      <div class="brand-name">Corwin's<small>Meadow Pine Flock Co.</small></div>
    </div>
  </section>
</main>
</body>
</html>
```